Simple 4 page brochure design - Duplex printable pdf document - A3 format

We are language training company based in France and need :

* Duplex printable pdf document on standard office printer (not professional printer). Once printed, document should fold in two and form a brochure.
* Format : A3 + optional A4 version (European settings)
* Attached zip file contains all elements necessary to complete the work:
- power point specification (written in English and French)
- preliminary design considered as non-satisfactory
- word document with copy / paste content in French and preferred layout
- logos
* Document should be on white background, free of clutter and business like.
* No illustration work necessary, but simple elements of design need to be included to project quality and professionnalism
* We also need an illustration / pictogram for point 4 ('Livret d'apprentissage' which is a learning booklet, to be found in Folder 'Copy Paste Documents' 'Layout and Copy Past' in Word

We need to receive elements within the next 36 to 48 hours to be able to decide on winning design and place order beginning of next week (Monday April 28).

Thank you to all who will take the time to respond.

Reason: Deadline extended to include the whole week-end as no decision will be taken before the beginning of next week.

```html
<!DOCTYPE html>
<html lang="fr">
<head>
<meta charset="utf-8">
<title>Lingua Pont – Formations et services linguistiques</title>
<link href="https://fonts.googleapis.com/css2?family=Open+Sans:wght@400;600;700;800&display=swap" rel="stylesheet">
<style>
:root{
  --green:#8cbd2e;
  --green-dark:#6f9c1c;
  --green-pale:#e6efc7;
  --green-line:#b9d57a;
  --text:#5a5a5a;
  --ink:#3d3d3d;
  --paper:#ffffff;
  --badge-blue:#2c86b8;
}
*{box-sizing:border-box;margin:0;padding:0}
html,body{width:1200px;height:848px;overflow:hidden;background:var(--paper)}
body{font-family:"Open Sans",Arial,sans-serif;color:var(--text);position:relative}

/* ---------- left page ---------- */
.page-left{position:absolute;left:0;top:0;width:600px;height:848px}
.brand{position:absolute;left:46px;top:52px;display:flex;align-items:center;gap:8px}
.brand-dot{width:16px;height:16px;border-radius:50%;background:var(--green)}
.brand-name{font-weight:800;font-size:22px;color:var(--green);letter-spacing:.5px}

.intro{position:absolute;left:57px;top:138px;width:385px}
.section-title{font-size:14.5px;font-weight:800;color:var(--green);letter-spacing:.2px;margin-bottom:6px}
.intro p{font-size:10.4px;line-height:1.42;margin-bottom:10px;color:var(--ink)}
.pillars{list-style:none}
.pillars li{position:relative;padding-left:14px;font-size:10.4px;line-height:1.42;margin-bottom:10px;color:var(--ink)}
.pillars li::before{content:"";position:absolute;left:0;top:5px;width:6px;height:6px;border-radius:50%;background:var(--green)}
.pillars strong{font-weight:700;color:var(--ink)}
.pillars .sep{color:var(--green);font-weight:700;margin:0 3px}

.network{position:absolute;left:455px;top:150px;width:135px}
.network-name{display:flex;align-items:center;gap:6px;margin-bottom:16px}
.network-square{width:14px;height:14px;background:var(--badge-blue)}
.network-name span{font-size:16px;font-weight:700;color:var(--badge-blue)}
.network h3{font-size:11px;font-weight:700;color:var(--green);line-height:1.35;margin-bottom:8px}
.network p{font-size:10px;line-height:1.4;color:var(--green-dark)}

.tools{position:absolute;left:57px;top:598px;width:385px}
.tool{margin-top:9px}
.tool h4{font-size:10.6px;font-weight:700;color:var(--green);margin-bottom:2px}
.tool p{font-size:10px;line-height:1.38;color:var(--ink)}

.tool-marks{position:absolute;left:548px;top:638px;width:60px}
.mark{display:block;margin:0 auto 14px}
.mark-rect{width:56px;height:34px;background:#2f6fb3;border-radius:2px}
.mark-round{width:44px;height:44px;border-radius:50%;background:#9ccc4a}
.mark-seal{width:40px;height:40px;border-radius:50%;background:#e3a43a}
.mark-booklet{width:40px;height:40px;border-radius:4px;background:linear-gradient(135deg,#d9d9d9,#9a9a9a)}

/* ---------- right page ---------- */
.page-right{position:absolute;left:600px;top:0;width:600px;height:848px}
.plan{position:absolute;left:-105px;top:136px;width:810px;height:575px;transform:rotate(-90deg);transform-origin:center}
.plan-bar{height:24px;background:var(--green);color:#fff;font-weight:800;font-size:12px;letter-spacing:1px;padding:4px 10px}
.plan-table{width:100%;border-collapse:collapse;table-layout:fixed;margin-top:4px}
.plan-table th,.plan-table td{border:1px solid var(--green-line);padding:3px 4px;font-size:7.6px;line-height:1.3;vertical-align:top;text-align:left;color:var(--ink)}
.plan-table thead th{background:var(--green-pale);font-weight:700;color:var(--green-dark)}
.plan-table tbody th{background:var(--green-pale);font-weight:700;color:var(--green-dark);width:78px}
.plan-table ul{list-style:none}
.plan-table li{padding-left:7px;position:relative}
.plan-table li::before{content:"•";position:absolute;left:0;color:var(--green)}
.row-obj td{height:140px}
.row-price td{height:98px}
</style>
</head>
<body>

<section class="page-left">
  <div class="brand"><span class="brand-dot"></span><span class="brand-name">Lingua Pont</span></div>

  <div class="intro">
    <h2 class="section-title">FORMATIONS ET SERVICES LINGUISTIQUES</h2>
    <p>Lingua Pont Services (LPS) est une école de langues fondée en 1988, aujourd'hui installée à Paris-Ouest, et intervient principalement auprès de grands comptes.</p>
    <p>LPS préconise et déploie des dispositifs de formation reposant sur le principe de la mise en situation professionnelle, le seul à même d'augmenter réellement et durablement la capacité des collaborateurs de l'entreprise à pratiquer leur métier dans une langue étrangère (anglais, langue européenne ou langue rare).</p>
    <p>La démarche d'LPS est orientée résultats (opérationnalité et progression des apprenants) et repose sur les piliers suivants :</p>
    <ul class="pillars">
      <li><strong>L'excellence pédagogique</strong><span class="sep">/</span>La méthodologie d'LPS, une des premières à s'appuyer sur des référentiels de compétences professionnelles, a été validée dans la durée par les plus grandes entreprises (Énergia, Nucléo, Banque Horizon, Aérotek, Belmonde, Petrolis, Auditis, …).</li>
      <li><strong>Un corps enseignant expérimenté</strong><span class="sep">/</span>Nos professeurs, dont certains sont habilités à former des formateurs, disposent d'un double diplôme, universitaire et d'enseignement des langues, souvent complété par un parcours individuel en entreprise</li>
      <li><strong>Des réponses personnalisées</strong><span class="sep">/</span>Notre équipe pédagogique décidée puise dans l'expérience collective d'LPS, pédagogique et sectorielle, pour développer des contenus originaux et assurer leur pertinence dans la durée</li>
      <li><strong>L'intégration des nouvelles technologies</strong><span class="sep">/</span>LPS s'appuie sur plusieurs outils du marché en fonction des contextes, et développe sur plate-forme propre des parcours en Blended Learning aux contenus personnalisés, parfaitement reliés aux enseignements dispensés dans les modalités traditionnelles</li>
    </ul>
  </div>

  <aside class="network">
    <div class="network-name"><span class="network-square"></span><span>Parlia</span></div>
    <h3>LPS est un membre et actionnaire historique de Parlia</h3>
    <p>Le 1er réseau qui réunit les meilleurs centres indépendants de formation linguistique en France (26 centres couvrant tout le territoire), avec membres associés dans plusieurs pays européens.</p>
  </aside>

  <div class="tools">
    <h2 class="section-title">LES OUTILS DE DÉPLOIEMENT</h2>
    <div class="tool"><h4>Evaluation linguistique</h4><p>Une évaluation complète (compréhension orale, écrite, production orale, écrite) reliée aux niveaux du Cadre Européen Commun de Référence</p></div>
    <div class="tool"><h4>Détermination des besoins</h4><p>Un recueil automatisé des besoins suivi d'un diagnostic individuel, du positionnement dans le parcours adéquat, de la mise en groupe et accès au modèle économique en temps direct</p></div>
    <div class="tool"><h4>E-learning</h4><p>E-learning conçu spécifiquement pour la Banque Horizon, avec des supports diversifiés et des activités motivantes reliées aux objectifs d'apprentissage</p></div>
    <div class="tool"><h4>Livret d'apprentissage</h4><p>Un support individuel fourni en début de parcours pour créer le lien entre les différentes modalités</p></div>
  </div>

  <div class="tool-marks">
    <span class="mark mark-rect" role="img" aria-label="Badge partenaire évaluation"></span>
    <span class="mark mark-round" role="img" aria-label="Badge partenaire e-learning"></span>
    <span class="mark mark-seal" role="img" aria-label="Sceau anniversaire de l'école"></span>
    <span class="mark mark-booklet" role="img" aria-label="Pictogramme d'un livret d'apprentissage et d'un stylo"></span>
  </div>
</section>

<section class="page-right">
  <div class="plan">
    <div class="plan-bar">VOTRE DISPOSITIF</div>
    <table class="plan-table">
      <thead>
        <tr>
          <th style="width:78px">Parcours</th>
          <th>Anglais Standard 1 – S'exprimer avec aisance</th>
          <th>Anglais 2 – Semaines intensives à Paris</th>
          <th>Anglais 3 – Semaines intensives à l'étranger</th>
          <th>Anglais 4 – Formation préparatoire Britannia</th>
          <th>Anglais 5 – Cours particuliers</th>
          <th>Anglais 6 – Cours de perfectionnement</th>
        </tr>
      </thead>
      <tbody>
        <tr><th>Public</th>
          <td>Toute personne devant utiliser le téléphone et les réunions en anglais au quotidien</td>
          <td>Toute personne désirant augmenter rapidement son niveau de langue</td>
          <td>Toute personne devant progresser en immersion complète</td>
          <td>Tout public souhaitant valider son niveau par un examen</td>
          <td>Tout public désirant un suivi individuel sur mesure</td>
          <td>Tout public désirant perfectionner sa langue professionnelle</td></tr>
        <tr><th>Niveau</th>
          <td>Fondamentaux</td><td>Perfectionnement</td><td>Perfectionnement</td><td>Intermédiaire</td><td>Fondamentaux</td><td>Perfectionnement</td></tr>
        <tr><th>Durée</th>
          <td>20 heures</td><td>40 heures</td><td>40 heures</td><td>20 heures</td><td>15 heures</td><td>15 heures</td></tr>
        <tr><th>Rythme</th>
          <td>20 h en présentiel et 10 h d'e-learning sur trois mois</td>
          <td>40 h en présentiel sur deux semaines</td>
          <td>Séjour linguistique de deux semaines</td>
          <td>20 h de face à face individuel</td>
          <td>15 h en présentiel, séances de 1 h 30</td>
          <td>15 h en présentiel, séances de 1 h 30</td></tr>
        <tr><th>Format</th>
          <td>Blended Learning</td><td>Présentiel</td><td>Présentiel</td><td>Présentiel</td><td>Présentiel</td><td>Présentiel</td></tr>
        <tr class="row-obj"><th>Objectifs</th>
          <td><ul><li>S'exprimer avec aisance au téléphone</li><li>Participer à des réunions</li><li>Rédiger des courriels clairs</li><li>Être opérationnel sur le poste de travail</li></ul></td>
          <td><ul><li>S'exprimer avec fluidité</li><li>Gagner en confiance à l'oral</li><li>Être opérationnel sur le poste de travail</li></ul></td>
          <td><ul><li>Se présenter et dialoguer en situation réelle</li><li>Comprendre les échanges courants</li><li>Être autonome en voyage</li></ul></td>
          <td><ul><li>Maîtriser les structures grammaticales</li><li>Enrichir le vocabulaire</li><li>Préparer les épreuves écrites et orales</li></ul></td>
          <td><ul><li>Consolider les bases grammaticales</li><li>Améliorer la compréhension orale</li><li>S'exprimer sur son métier</li></ul></td>
          <td><ul><li>Maîtriser les expressions idiomatiques</li><li>Affiner la compréhension de textes professionnels</li></ul></td></tr>
        <tr class="row-price"><th>Prix par apprenant</th>
          <td>INTER : 420 € HT par apprenant ; INTRA : 3 200 € HT par groupe de six</td>
          <td>INTER : 1 250 € HT par apprenant ; INTRA : 6 400 € HT par groupe</td>
          <td>Selon destination : 2 100 € à 2 800 € HT, hébergement compris</td>
          <td>INTRA : 1 150 € HT par apprenant, examen inclus</td>
          <td>1 050 € HT par apprenant, supports compris</td>
          <td>1 050 € HT par apprenant, supports compris</td></tr>
      </tbody>
    </table>
  </div>
</section>

</body>
</html>
```